Business Card Design

Need a hot business card in wine colors something cool and mod please feel free to be , FUNKY and free with this .
Updates

Industry/Entity Type

Business

Contact Information for Business Card

KALIMERO HAIR DESIGN 2918 w 3rd st scottsdale az 85019 Custom modern hair design and custom color by MARCUS DOVELING 602-4813926 cell salon 480 -317-2064 email marcusdoveling@plumbox.net hours wed thru sat 7am to 6pm.

Font styles to use
Other font styles liked:
• something fun and mod.

Colors
a54599
6b449b
1b1b1b
606060

Requirements
Must have
• Apointment reminder on flip side of card.
Should not have
• Nothing boring.

```html
<!DOCTYPE html>
<html lang="en">
<head>
<meta charset="utf-8">
<title>Kalimero Hair Design – Business Card</title>
<link rel="stylesheet" href="https://fonts.googleapis.com/css2?family=Federo&family=Sorts+Mill+Goudy&display=swap">
<style>
  :root {
    --ink: #04040a;
    --night: #0d1038;
    --violet: #a11ff0;
    --electric: #4b26ff;
    --violet-text: #a23de6;
    --electric-text: #5a3cf5;
    --white: #ffffff;
    --rule: #111111;
  }
  html, body {
    margin: 0;
    padding: 0;
    width: 1200px;
    height: 702px;
    overflow: hidden;
    background: var(--ink);
  }
  .card {
    position: relative;
    width: 1200px;
    height: 702px;
    overflow: hidden;
    background: var(--ink);
  }
  .card__backdrop {
    position: absolute;
    inset: 0;
    background:
      radial-gradient(ellipse at 30% 95%, #1a1f5e 0%, rgba(13,16,56,0.6) 35%, transparent 65%),
      radial-gradient(ellipse at 80% 70%, #14184a 0%, transparent 55%),
      linear-gradient(180deg, #020205 0%, #05061a 45%, var(--night) 100%);
  }
  .band {
    position: absolute;
    left: 0;
    width: 1200px;
  }
  .band--top { top: 107px; height: 36px; background: var(--electric); }
  .band--main { top: 142px; height: 176px; background: var(--violet); }
  .band--seam { top: 317px; height: 3px; background: #3a0f7a; }
  .band--bottom { top: 320px; height: 34px; background: var(--electric); }

  .name-rule {
    position: absolute;
    top: 280px;
    height: 4px;
    background: var(--rule);
  }
  .name-rule--left { left: 0; width: 337px; }
  .name-rule--right { left: 894px; width: 306px; }

  .brand {
    position: absolute;
    left: 70px;
    top: 92px;
    margin: 0;
    font-family: "Federo", sans-serif;
    font-weight: 400;
    font-size: 124px;
    line-height: 1;
    color: var(--white);
    letter-spacing: 2px;
  }
  .brand__tagline {
    position: absolute;
    left: 804px;
    top: 158px;
    font-family: "Federo", sans-serif;
    font-size: 46px;
    line-height: 1;
    color: var(--white);
    letter-spacing: 1px;
  }
  .stylist {
    position: absolute;
    left: 337px;
    width: 557px;
    top: 258px;
    text-align: center;
    font-family: "Federo", sans-serif;
    font-size: 44px;
    line-height: 1;
    color: var(--rule);
    letter-spacing: 1px;
  }

  .contact {
    font-family: "Sorts Mill Goudy", serif;
    font-size: 46px;
    line-height: 1;
    position: absolute;
  }
  .address { left: 55px; top: 402px; }
  .address__street { color: var(--white); margin: 0 0 11px; }
  .address__city { color: var(--electric-text); margin: 0; }

  .phones { right: 44px; top: 402px; text-align: right; }
  .phones p { margin: 0 0 11px; }
  .phones__label--cell { color: var(--white); }
  .phones__number--cell { color: var(--electric-text); }
  .phones__label--salon { color: var(--violet-text); }
  .phones__number--salon { color: var(--white); }
  .phones__dot { color: var(--violet-text); }
  .gap { display: inline-block; width: 22px; }

  .divider {
    position: absolute;
    left: 212px;
    top: 542px;
    width: 802px;
    height: 4px;
    background: var(--white);
  }
  .email {
    position: absolute;
    left: 0;
    width: 1244px;
    top: 572px;
    text-align: center;
    font-family: "Sorts Mill Goudy", serif;
    font-size: 43px;
    line-height: 1;
    color: var(--violet-text);
    margin: 0;
  }
</style>
</head>
<body>
  <main class="card">
    <div class="card__backdrop" role="img" aria-label="Dark blue close-up photograph of a model's hair and brow behind the card details"></div>

    <div class="band band--top"></div>
    <div class="band band--main"></div>
    <div class="band band--seam"></div>
    <div class="band band--bottom"></div>

    <h1 class="brand">Kalimero</h1>
    <div class="brand__tagline">HAIR DESIGN</div>

    <div class="name-rule name-rule--left"></div>
    <div class="stylist">MARCUS DOVELING</div>
    <div class="name-rule name-rule--right"></div>

    <address class="contact address" style="font-style:normal">
      <p class="address__street">2918 W 3rd St</p>
      <p class="address__city">Scottsdale AZ 85019</p>
    </address>

    <div class="contact phones">
      <p><span class="phones__label--cell">Cell</span><span class="gap"></span><span class="phones__number--cell">602.481.3926</span></p>
      <p><span class="phones__label--salon">Salon</span> <span class="phones__number--salon">480<span class="phones__dot">.</span>317<span class="phones__dot">.</span>2064</span></p>
    </div>

    <div class="divider"></div>
    <p class="email">MarcusDoveling@plumbox.net</p>
  </main>
</body>
</html>
```